Ad to be used on social media.

____________________________________________________________________________

Bored at Home?

Study to become a
Virtual Mortgage Originator today...

Complete 20 Hour Online Course & State Exam
in 30 days or less

Earn $3,000 to $5,000 on average per loan
No Work Hours, Goals or Quotas
Full Time or Part Time Opportunities

Email us at employment@brightlanehome.com

Oakmere Lending Group, Inc.
7200 Wexbury Lane
Ellicott City, MD 21043
(800) 461-9027
www.brightlanehome.com
NMLS #738160

```html
<!DOCTYPE html>
<html lang="en">
<head>
<meta charset="utf-8">
<title>Bored at Home? – Virtual Mortgage Originator</title>
<link rel="stylesheet" href="https://fonts.googleapis.com/css2?family=Bebas+Neue&family=Roboto+Condensed:wght@700&display=swap">
<style>
  :root {
    --teal: #17b3c3;
    --navy: #1d2437;
    --coral: #e2594c;
    --yellow: #fbc02a;
    --ink: #2a2a2a;
    --band: #141414;
    --white: #ffffff;
  }
  * { margin: 0; padding: 0; box-sizing: border-box; }
  html, body { width: 849px; height: 1200px; overflow: hidden; background: var(--teal); }
  .ad { position: relative; width: 849px; height: 1200px; background: var(--teal); font-family: "Roboto Condensed", "Arial Narrow", sans-serif; }

  .collage { position: absolute; left: 36px; top: 46px; width: 763px; height: 510px; background: var(--white); }
  .tile { position: absolute; }
  .tile-1 { left: 4px;   top: 4px;   width: 248px; height: 250px; background: linear-gradient(135deg, #c9a48a, #7d5a48); }
  .tile-2 { left: 257px; top: 4px;   width: 247px; height: 250px; background: linear-gradient(135deg, #e9e4df, #8895a6); }
  .tile-3 { left: 509px; top: 4px;   width: 250px; height: 250px; background: linear-gradient(135deg, #efe7dd, #d56a5c); }
  .tile-4 { left: 4px;   top: 259px; width: 374px; height: 247px; background: linear-gradient(135deg, #eee7de, #8a6a58); }
  .tile-5 { left: 383px; top: 259px; width: 376px; height: 247px; background: linear-gradient(135deg, #c8c8c6, #5f86b0); }

  .badge { position: absolute; left: 267px; top: 134px; width: 310px; height: 310px; border-radius: 50%; background: var(--white); }
  .badge-inner { position: absolute; left: 12px; top: 12px; width: 286px; height: 286px; border-radius: 50%; background: var(--yellow); text-align: center; }
  .badge-face { position: absolute; left: 108px; top: 40px; }
  .badge-title { position: absolute; left: 0; right: 0; top: 112px; font-family: "Bebas Neue", "Oswald", sans-serif; font-size: 70px; line-height: 64px; color: var(--ink); }

  .headline { position: absolute; left: 80px; top: 586px; font-family: "Bebas Neue", "Oswald", sans-serif; font-size: 48px; line-height: 48px; color: var(--navy); letter-spacing: 0.3px; }
  .course { position: absolute; left: 80px; top: 714px; font-size: 30px; line-height: 40px; color: var(--coral); }

  .perks { position: absolute; top: 838px; list-style: none; font-size: 33px; line-height: 40px; color: var(--navy); }
  .perks-left { left: 52px; }
  .perks-right { left: 470px; }
  .perks li { position: relative; padding-left: 32px; }
  .perks li svg { position: absolute; left: 0; top: 9px; }
  .perks-left li + li { margin-top: 0; }

  .contact-band { position: absolute; left: 0; top: 998px; width: 849px; height: 48px; background: var(--band); color: var(--white); font-size: 32px; line-height: 48px; text-align: center; }

  .company { position: absolute; left: 0; right: 0; top: 1062px; text-align: center; font-size: 26px; line-height: 35px; color: var(--navy); }
</style>
</head>
<body>
<main class="ad">
  <section class="collage">
    <div class="tile tile-1" role="img" aria-label="Photo of a bored young woman holding a TV remote"></div>
    <div class="tile tile-2" role="img" aria-label="Photo of a bored woman sitting on a sofa"></div>
    <div class="tile tile-3" role="img" aria-label="Photo of a bored woman on a couch with a remote"></div>
    <div class="tile tile-4" role="img" aria-label="Photo of a smiling woman working on a laptop"></div>
    <div class="tile tile-5" role="img" aria-label="Photo of a woman typing on a laptop on a sofa"></div>

    <div class="badge">
      <div class="badge-inner">
        <svg class="badge-face" width="70" height="64" viewBox="0 0 70 64" aria-hidden="true">
          <rect x="4" y="4" width="22" height="5" rx="2.5" fill="#2a2a2a"/>
          <rect x="44" y="4" width="22" height="5" rx="2.5" fill="#2a2a2a"/>
          <path d="M6 20 a9 8 0 0 0 18 0 Z" fill="#2a2a2a"/>
          <path d="M46 20 a9 8 0 0 0 18 0 Z" fill="#2a2a2a"/>
          <path d="M18 58 Q35 42 52 58" fill="none" stroke="#2a2a2a" stroke-width="5" stroke-linecap="round"/>
        </svg>
        <h1 class="badge-title">Bored at<br>Home?</h1>
      </div>
    </div>
  </section>

  <h2 class="headline">Study to become a virtual<br>mortgage originator today...</h2>
  <p class="course">Complete 20 Hour Online Course<br>&amp; State Exam in 30 days or less</p>

  <ul class="perks perks-left">
    <li><svg width="18" height="20" viewBox="0 0 18 20" aria-hidden="true"><path d="M2 1v18" stroke="#e2594c" stroke-width="2.5"/><path d="M3 2 L16 7 L3 12 Z" fill="#e2594c"/></svg>Earn $3,000 to $5,000<br>on average per loan</li>
    <li><svg width="18" height="20" viewBox="0 0 18 20" aria-hidden="true"><path d="M2 1v18" stroke="#e2594c" stroke-width="2.5"/><path d="M3 2 L16 7 L3 12 Z" fill="#e2594c"/></svg>No Work Hours,</li>
  </ul>
  <ul class="perks perks-right">
    <li><svg width="18" height="20" viewBox="0 0 18 20" aria-hidden="true"><path d="M2 1v18" stroke="#e2594c" stroke-width="2.5"/><path d="M3 2 L16 7 L3 12 Z" fill="#e2594c"/></svg>Goals or Quotas</li>
    <li><svg width="18" height="20" viewBox="0 0 18 20" aria-hidden="true"><path d="M2 1v18" stroke="#e2594c" stroke-width="2.5"/><path d="M3 2 L16 7 L3 12 Z" fill="#e2594c"/></svg>Full Time or Part<br>Time Opportunities</li>
  </ul>

  <div class="contact-band">Email us at employment@brightlanehome.com</div>

  <address class="company" style="font-style:normal">
    Oakmere Lending Group, Inc.<br>
    7200 Wexbury Lane, Ellicott City, MD 21043<br>
    (800) 461-9027, www.brightlanehome.com, NMLS #738160
  </address>
</main>
</body>
</html>
```